Stationary and Business Card for Law Firm
Modern, Professional & Sophisticated Law Firm Card
Stationary and Business Card for Law Firm - Law
Creative Brief
Professional
Owen Barker
Partner
482 North Mill Avenue Pelham, Illinois 62904
obarker@barkerwynn.example
www.barkerwynn.example
These cards will be used by three attorneys, so I would like to be able to change the names out. Alternatively, if you could insert the names when providing source files, it would be appreciated. Names are: Owen B. Barker Rosalind P. Barker Natalie K. Wynn Emails are: obarker@barkerwynn.example rbarker@barkerwynn.example nwynn@barkerwynn.example
pbruner27 pbruner27
While I like the look many of the envelopes, the return address must be in the upper right hand corner to meet US Postal regulations. Firm Name/Logo Address City, State Zip (additional design info if you like) I have had similar envelopes on a different project with the Logo address on the lower part of the envelope---the post office refused to accept them.

```html
<!DOCTYPE html>
<html lang="en">
<head>
<meta charset="utf-8">
<title>Barker &amp; Wynn Stationery</title>
<link href="https://fonts.googleapis.com/css2?family=Cinzel:wght@400&family=Work+Sans:wght@400;500&display=swap" rel="stylesheet">
<style>
  :root {
    --tan: #c6a57a;
    --ink: #1f1f1f;
    --grey: #6f6f6f;
    --text: #4a4a4a;
    --paper: #ffffff;
    --bg: #f1f1f1;
    --shadow: 0 1px 4px rgba(0,0,0,.18);
  }
  * { box-sizing: border-box; margin: 0; padding: 0; }
  html, body { width: 1200px; height: 828px; overflow: hidden; background: var(--bg); }
  body { position: relative; font-family: "Work Sans", Arial, sans-serif; color: var(--text); }

  .sheet { position: absolute; background: var(--paper); box-shadow: var(--shadow); overflow: hidden; }

  .brand { display: flex; align-items: center; gap: 8px; position: absolute; }
  .brand-square { background: var(--tan); flex: none; }
  .brand-name { font-family: "Cinzel", Georgia, serif; color: var(--grey); font-weight: 400; white-space: nowrap; line-height: 1; }

  .contact { position: absolute; font-size: 8px; line-height: 11px; color: var(--text); }
  .contact li { list-style: none; display: flex; align-items: center; gap: 4px; }
  .contact .dot { width: 3px; height: 3px; background: var(--tan); flex: none; }

  .bands { position: absolute; left: 0; bottom: 0; width: 100%; }

  /* Letterhead */
  .letterhead { left: 48px; top: 24px; width: 540px; height: 780px; }
  .letterhead .brand { left: 34px; top: 42px; }
  .letterhead .brand-square { width: 26px; height: 26px; }
  .letterhead .brand-name { font-size: 26px; }
  .letterhead .divider { position: absolute; left: 281px; top: 26px; width: 1px; height: 70px; background: var(--tan); }
  .letterhead .contact { left: 300px; top: 32px; font-size: 8.5px; line-height: 12px; }
  .letter { position: absolute; left: 34px; top: 262px; width: 440px; font-size: 10.5px; line-height: 14px; }
  .letter .salutation { font-size: 14px; color: var(--ink); margin-bottom: 14px; }
  .letter p { margin-bottom: 13px; }
  .letter .closing { margin-top: 22px; font-size: 10.5px; color: var(--ink); }
  .signature { width: 110px; height: 20px; margin-top: 6px; background: linear-gradient(90deg, #d8d8d8, #efefef); border-radius: 10px; }

  /* Business card front */
  .card-front { left: 619px; top: 19px; width: 269px; height: 150px; }
  .card-front .brand { left: 16px; top: 52px; gap: 5px; }
  .card-front .brand-square { width: 14px; height: 14px; }
  .card-front .brand-name { font-size: 14px; }
  .card-front .divider { position: absolute; left: 142px; top: 18px; width: 1px; height: 104px; background: #d4d4d4; }
  .card-front .person { position: absolute; left: 152px; top: 18px; }
  .card-front .person-name { font-size: 10px; letter-spacing: 1px; color: var(--tan); font-weight: 500; text-transform: uppercase; }
  .card-front .person-role { font-size: 7px; color: var(--text); margin-top: 1px; }
  .card-front .contact { left: 152px; top: 48px; font-size: 6.5px; line-height: 9px; }

  /* Business card back */
  .card-back { left: 912px; top: 19px; width: 271px; height: 150px; background: var(--ink); }
  .card-back .brand { left: 56px; top: 60px; gap: 6px; }
  .card-back .brand-square { width: 18px; height: 18px; }
  .card-back .brand-name { font-size: 18px; color: #fff; }
  .card-back .web { position: absolute; right: 14px; bottom: 10px; font-size: 6.5px; color: #cfcfcf; }

  /* Envelope front */
  .env-front { left: 619px; top: 221px; width: 564px; height: 283px; }
  .env-front .brand { left: 24px; top: 38px; gap: 6px; }
  .env-front .brand-square { width: 22px; height: 22px; }
  .env-front .brand-name { font-size: 22px; }
  .env-front .address { position: absolute; left: 24px; top: 76px; font-size: 8px; line-height: 11px; width: 170px; }
  .env-front .contact { left: 24px; top: 176px; }

  /* Envelope back */
  .env-back { left: 619px; top: 523px; width: 564px; height: 286px; }
  .env-back .flap { position: absolute; left: 0; top: 0; width: 564px; height: 120px; }
  .env-back .flap-name { position: absolute; left: 0; right: 0; top: 36px; text-align: center; font-family: "Cinzel", Georgia, serif; font-size: 22px; color: #fff; }
  .env-back .seal { position: absolute; left: 262px; top: 186px; width: 40px; height: 40px; background: var(--tan); }
</style>
</head>
<body>

<section class="sheet letterhead">
  <div class="brand">
    <span class="brand-square"></span>
    <span class="brand-name">Barker &amp; Wynn</span>
  </div>
  <span class="divider"></span>
  <ul class="contact">
    <li>482 North Mill Avenue</li>
    <li>Pelham, Illinois 62904</li>
    <li><span class="dot"></span>555.014.2271</li>
    <li><span class="dot"></span>555.014.2290</li>
    <li><span class="dot"></span>obarker@barkerwynn.example</li>
    <li><span class="dot"></span>www.barkerwynn.example</li>
  </ul>
  <article class="letter">
    <p class="salutation">Dear Sir</p>
    <p>Thank you for choosing our firm to represent your interests. We have reviewed the documents you provided and prepared a short summary of the next steps in your matter. Please read the notes below and contact our office with any questions you may have.</p>
    <p>Our attorneys will meet with the other party next week to discuss the terms of the agreement. We expect a written response shortly after that meeting and will forward a copy to you as soon as it arrives at our office here.</p>
    <p>In the meantime, please gather any receipts, letters or records related to the property. These items will help us build a clear timeline and support the position we will present on your behalf during the coming weeks of review.</p>
    <p>We appreciate your trust and look forward to working with you. Should your situation change in any way, let us know right away so that we can adjust our approach and keep your matter moving forward without delay.</p>
    <p class="closing">Kind Regards</p>
    <div class="signature" role="img" aria-label="Handwritten signature"></div>
  </article>
  <svg class="bands" width="540" height="14" viewBox="0 0 540 14" aria-hidden="true">
    <polygon points="290,14 300,4 420,4 410,14" fill="var(--tan)"/>
    <polygon points="410,14 420,4 540,4 540,14" fill="var(--ink)"/>
  </svg>
</section>

<section class="sheet card-front">
  <div class="brand">
    <span class="brand-square"></span>
    <span class="brand-name">Barker &amp; Wynn</span>
  </div>
  <span class="divider"></span>
  <div class="person">
    <p class="person-name">Owen Barker</p>
    <p class="person-role">Partner</p>
  </div>
  <ul class="contact">
    <li>482 North Mill Avenue</li>
    <li>Pelham, Illinois 62904</li>
    <li>555.014.2271</li>
    <li>555.014.2290</li>
    <li>obarker@barkerwynn.example</li>
    <li>www.barkerwynn.example</li>
  </ul>
  <svg class="bands" width="269" height="8" viewBox="0 0 269 8" aria-hidden="true">
    <polygon points="0,8 0,3 150,3 145,8" fill="var(--tan)"/>
    <polygon points="145,8 150,3 269,3 269,8" fill="var(--ink)"/>
  </svg>
</section>

<section class="sheet card-back">
  <div class="brand">
    <span class="brand-square"></span>
    <span class="brand-name">Barker &amp; Wynn</span>
  </div>
  <p class="web">www.barkerwynn.example</p>
</section>

<section class="sheet env-front">
  <div class="brand">
    <span class="brand-square"></span>
    <span class="brand-name">Barker &amp; Wynn</span>
  </div>
  <p class="address">482 North Mill Avenue<br>Pelham, Illinois 62904</p>
  <ul class="contact">
    <li><span class="dot"></span>555.014.2271</li>
    <li><span class="dot"></span>555.014.2290</li>
    <li><span class="dot"></span>obarker@barkerwynn.example</li>
    <li><span class="dot"></span>www.barkerwynn.example</li>
  </ul>
  <svg class="bands" width="564" height="14" viewBox="0 0 564 14" aria-hidden="true">
    <polygon points="0,14 0,9 180,9 175,14" fill="var(--tan)"/>
    <polygon points="175,14 188,1 564,1 564,14" fill="var(--ink)"/>
  </svg>
</section>

<section class="sheet env-back">
  <svg class="flap" width="564" height="120" viewBox="0 0 564 120" aria-hidden="true">
    <path d="M0,0 H564 V70 Q564,112 520,112 H44 Q0,112 0,70 Z" fill="var(--ink)"/>
  </svg>
  <p class="flap-name">Barker &amp; Wynn</p>
  <span class="seal"></span>
</section>

</body>
</html>
```